Lantern Advisory Website

I currently have a website www.lanternadvisoryinc.example. We are a IT Consulting Company. Our website will pretty much tell out our services. I am looking to enhance my website and make it look more professional. Looking for very classy and Contemporary look and design for my website.

It Company

```html
<!DOCTYPE html>
<html lang="en">
<head>
<meta charset="utf-8">
<title>Lantern Advisory</title>
<link href="https://fonts.googleapis.com/css2?family=Montserrat:wght@400;500;600;700&display=swap" rel="stylesheet">
<style>
:root{
  --blue:#1e62a8;
  --blue-top:#1b5a9e;
  --navy:#0f3266;
  --navy-deep:#0b2a57;
  --sky:#29a3dc;
  --dark:#232323;
  --grey-bg:#f2f2f2;
  --text:#555;
  --white:#fff;
}
*{margin:0;padding:0;box-sizing:border-box}
html,body{width:1200px;height:3203px;overflow:hidden}
body{font-family:'Montserrat',sans-serif;color:var(--text);background:var(--white);position:relative}
.abs{position:absolute}
svg{display:block}

.topbar{left:0;top:0;width:1200px;height:36px;background:var(--blue-top);color:var(--white);font-size:10px}
.topbar .item{top:11px;display:flex;align-items:center;gap:6px;white-space:nowrap}
.topbar .social{top:10px;left:967px;display:flex;gap:6px}
.topbar .social span{width:12px;height:12px;border-radius:50%;background:rgba(255,255,255,.8)}

.hero{left:0;top:36px;width:1200px;height:540px;background:linear-gradient(160deg,#e9eef3 0%,#c9d6e2 40%,#aebfcf 70%,#d8dfe6 100%)}
.header{left:0;top:36px;width:1200px;height:86px;background:rgba(255,255,255,.88)}
.brand{display:flex;align-items:center;gap:8px;font-weight:700;color:var(--blue);font-size:22px;white-space:nowrap}
.brand .mark{width:30px;height:30px;background:var(--blue)}
.nav{left:604px;top:72px;font-size:12px;font-weight:500;color:var(--blue)}
.nav span{position:absolute;white-space:nowrap}
.dropdown{left:666px;top:100px;width:171px;background:var(--white);box-shadow:0 2px 6px rgba(0,0,0,.2);padding:8px 14px;font-size:11px;color:#222;z-index:5}
.dropdown li{list-style:none;line-height:23.5px;white-space:nowrap}
.hero-title{left:561px;top:203px;width:447px;height:85px;background:rgba(40,40,40,.75);color:var(--white);font-size:21px;line-height:30px;padding:12px 16px;white-space:nowrap}
.dots{left:587px;top:540px;display:flex;gap:4px}
.dots span{width:9px;height:9px;border-radius:50%;background:#999}
.dots span:first-child{background:#ddd}

.band{left:0;top:576px;width:1200px;height:54px;background:var(--navy)}
.band-brand{left:186px;top:590px;color:var(--white);font-size:17px}
.band-brand .mark{background:var(--white);width:24px;height:24px}
.band-h24{left:380px;top:586px;color:var(--white);font-size:28px;font-weight:600}
.band-enquiry{left:600px;top:597px;width:226px;text-align:right;color:var(--white);font-size:12.5px;white-space:nowrap}
.band-phone{left:839px;top:591px;width:182px;height:26px;background:var(--white);color:var(--navy);font-size:14px;font-weight:600;display:flex;align-items:center;justify-content:center;gap:8px;white-space:nowrap}

.about{left:0;top:630px;width:1200px;height:288px;background:#f7f7f7}
.about-brand{left:522px;top:682px;color:#777;font-size:20px}
.about-brand .mark{background:#888;width:26px;height:26px}
.about-text{left:173px;top:743px;width:854px;text-align:center;font-size:11px;line-height:17px;color:#444}
.btn{background:var(--navy-deep);color:var(--white);font-size:11px;font-weight:600;text-align:center}
.about-btn{left:563px;top:845px;width:98px;height:25px;line-height:25px}

.card{top:958px;width:269px;height:186px}
.card.consult{left:173px;background:var(--navy)}
.card.consult .icon{left:16px;top:16px}
.card.consult h3{left:70px;top:40px;font-size:15px;font-weight:500;color:var(--white)}
.card.consult p{left:70px;top:66px;font-size:11px;line-height:17px;color:var(--white);width:180px}
.card.consult .more{left:70px;top:114px;font-size:10px;color:#cfd8e6}
.card.photo-staff{left:465px;background:linear-gradient(180deg,#6fa2d6,#b9c7d6 55%,#4b5a6b)}
.card.photo-rig{left:758px;background:linear-gradient(180deg,#3f7fc1,#7fb0dd 50%,#c79a5a)}
.card .bar{left:0;top:122px;width:269px;height:64px;background:rgba(11,42,87,.88);display:flex;align-items:center;gap:12px;padding-left:18px;color:var(--white);font-size:15px;font-weight:500}

.services{left:0;top:1208px;width:1200px;height:496px;background:var(--grey-bg)}
.sec-title{width:1200px;left:0;text-align:center;font-size:20px;color:#333;font-weight:500}
.sec-title::after{content:"";display:block;width:40px;height:2px;background:var(--blue);margin:6px auto 0}
.svc-hl{left:173px;top:1324px;width:269px;height:141px;background:var(--white)}
.svc-line{left:206px;top:1334px;width:2px;height:116px;background:var(--blue)}
.svc{width:250px}
.svc .hex{position:absolute;left:0;top:0}
.svc h4{position:absolute;left:60px;font-size:15px;font-weight:500;color:var(--blue);line-height:17px}
.svc p{position:absolute;left:60px;font-size:11px;line-height:16px;color:#555;width:200px}

.testi{left:0;top:1704px;width:1200px;height:363px;background:var(--blue)}
.testi-title{top:1762px;color:var(--white)}
.testi-title::after{display:none}
.t-photo{top:1864px;width:196px;height:137px}
.t-photo.p1{left:173px;background:linear-gradient(135deg,#d9d9d9,#9a9a9a)}
.t-photo.p2{left:611px;background:linear-gradient(135deg,#8a6a4a,#d8c08a)}
.t-body{top:1866px;width:200px;color:var(--white)}
.t-body h5{font-size:15px;font-weight:600}
.t-body .role{font-size:11px;font-weight:600;margin-top:2px}
.t-body p{font-size:11px;line-height:15px;margin-top:10px}

.callback{left:0;top:2067px;width:1200px;height:275px;background:var(--dark)}
.callback-title{left:181px;top:2165px;font-size:23px;font-weight:600;color:#ccc;line-height:29px}
.callback-label{left:470px;top:2139px;font-size:11px;color:#666}
.select{left:470px;top:2165px;width:262px;background:var(--white);font-size:11px;color:#555}
.select li{list-style:none;height:30px;line-height:30px;padding-left:20px}
.select li.top{border-bottom:1px solid #ddd;height:37px;line-height:37px}
.select li.active{background:var(--sky);color:var(--white)}
.input{background:var(--white);font-size:11px;color:#888;padding-left:20px;line-height:34px}
.callback-name{left:754px;top:2165px;width:264px;height:34px}
.callback-btn{left:754px;top:2225px;width:100px;height:37px;line-height:37px;font-size:14px;background:var(--blue)}

.map{left:0;top:2342px;width:1200px;height:333px;background:linear-gradient(120deg,#eceae6 0%,#e4e2dc 60%,#cfe0ef 85%,#9cc4ea 100%)}

.offices{left:0;top:2675px;width:1200px;height:218px;background:var(--blue)}
.office{top:2725px;width:240px;color:var(--white)}
.office h3{font-size:17px;font-weight:600;margin-bottom:14px}
.office .row{display:flex;gap:10px;font-size:11px;line-height:14px;margin-bottom:10px}
.divider-v{top:2720px;width:1px;height:130px;background:rgba(255,255,255,.35)}

.footer{left:0;top:2893px;width:1200px;height:256px;background:var(--blue);border-top:1px solid rgba(255,255,255,.25)}
.footer-brand{left:171px;top:2932px;color:#cdd9ea;font-size:19px}
.footer-brand .mark{background:#cdd9ea;width:24px;height:24px}
.footer-about{left:171px;top:2998px;width:215px;font-size:11px;line-height:15px;color:var(--white)}
.f-col{top:2950px;color:var(--white)}
.f-col h6{font-size:12px;font-weight:600;padding-bottom:10px;border-bottom:1px solid rgba(255,255,255,.35);width:180px}
.f-col ul{margin-top:14px}
.f-col li{list-style:none;font-size:11px;line-height:15px;padding-left:14px;position:relative}
.f-col li::before{content:"›";position:absolute;left:2px}
.f-col p{font-size:11px;line-height:15px;margin-top:14px;width:185px}
.sub-input{left:837px;top:3000px;width:165px;height:27px;line-height:27px;padding-left:10px;font-size:11px;color:#999;background:var(--white)}
.sub-btn{left:1002px;top:3000px;width:19px;height:27px;background:var(--sky)}
.sub-note{left:837px;top:3034px;font-size:11px;color:var(--white)}

.copy{left:0;top:3149px;width:1200px;height:54px;background:var(--blue);border-top:1px solid rgba(255,255,255,.25)}
.copy-txt{left:190px;top:3170px;font-size:11px;color:var(--white)}
.copy-social{left:903px;top:3164px;display:flex;gap:8px}
.copy-social span{width:25px;height:25px;border-radius:50%;background:var(--white)}
</style>
</head>
<body>

<div class="abs topbar">
  <div class="abs item" style="left:530px">
    <svg width="8" height="11" viewBox="0 0 8 11"><path d="M4 0a4 4 0 0 1 4 4c0 3-4 7-4 7S0 7 0 4a4 4 0 0 1 4-4z" fill="#fff"/></svg>
    410 Harbor Lane Suite 12 Eastbrook, NJ 07000
  </div>
  <div class="abs item" style="left:840px">
    <svg width="10" height="10" viewBox="0 0 10 10"><path d="M2 0l2 2.5-1.2 1.5a6 6 0 0 0 3.2 3.2L7.5 6 10 8 8.5 10C4 10 0 6 0 1.5z" fill="#fff"/></svg>
    +1 (555) 014 2290
  </div>
  <div class="abs social"><span></span><span></span><span></span><span></span></div>
</div>

<div class="abs hero" role="img" aria-label="Photo of a consultant presenting to a team at a meeting table"></div>
<div class="abs header"></div>
<div class="abs brand" style="left:192px;top:64px"><span class="mark"></span>Lantern Advisory</div>
<div class="abs nav">
  <span style="left:0">Company</span>
  <span style="left:79px;text-decoration:underline">Services</span>
  <span style="left:143px">Solutions</span>
  <span style="left:220px">Resources</span>
  <span style="left:299px">Career</span>
  <span style="left:359px">Contact Us</span>
</div>
<div class="abs hero-title">Delivering a New Level of Quality<br>Consultants and services</div>
<ul class="abs dropdown">
  <li>Technology</li><li>Business</li><li>Application Development</li><li>Enterprise Integration</li><li>IT Consulting</li><li>Research</li>
</ul>
<div class="abs dots"><span></span><span></span><span></span></div>

<div class="abs band"></div>
<div class="abs brand band-brand"><span class="mark"></span>Lantern Advisory</div>
<div class="abs band-h24">24x7</div>
<div class="abs band-enquiry">Call us today for enquiry</div>
<div class="abs band-phone">
  <svg width="12" height="12" viewBox="0 0 10 10"><path d="M2 0l2 2.5-1.2 1.5a6 6 0 0 0 3.2 3.2L7.5 6 10 8 8.5 10C4 10 0 6 0 1.5z" fill="#0f3266"/></svg>
  +1 (555) 014 2290
</div>

<div class="abs about"></div>
<div class="abs brand about-brand"><span class="mark"></span>Lantern Advisory</div>
<p class="abs about-text">Today's IT market is a dynamic, fast paced industry, with ever-increasing demands. Meeting these demands for over 25 years, Lantern Advisory maintains a global presence, aggressively recruiting expertly qualified IT and Management Professionals from around the world and cultivating key partnerships with corporations to understand their business models end to end, with a goal of delivering exceptional client service and ensuring a consistent delivery of the talent needed to drive results.</p>
<div class="abs btn about-btn">Read more</div>

<div class="abs card consult">
  <svg class="abs icon" width="44" height="30" viewBox="0 0 44 30"><path d="M2 10l10-6 8 4 6-3 16 6-6 10-8 5-10-6-10 0z" fill="#fff"/></svg>
  <h3 class="abs">Consulting</h3>
  <p class="abs">Lorem ipsum dolor sit amet, consectetuer adipiscing elit</p>
  <span class="abs more">Learn more</span>
</div>
<div class="abs card photo-staff" role="img" aria-label="Photo of a smiling team of staff">
  <div class="abs bar"><svg width="24" height="20" viewBox="0 0 24 20"><circle cx="12" cy="5" r="4" fill="#fff"/><circle cx="4" cy="8" r="3" fill="#fff"/><circle cx="20" cy="8" r="3" fill="#fff"/><path d="M5 20a7 7 0 0 1 14 0z" fill="#fff"/></svg>Staff Augmentation</div>
</div>
<div class="abs card photo-rig" role="img" aria-label="Photo of an offshore rig at sunset">
  <div class="abs bar"><svg width="22" height="22" viewBox="0 0 22 22"><circle cx="11" cy="11" r="9" fill="none" stroke="#fff" stroke-width="3"/><circle cx="11" cy="11" r="3" fill="#fff"/></svg>Offshore</div>
</div>

<div class="abs services"></div>
<div class="abs sec-title" style="top:1264px">Our Services</div>
<div class="abs svc-hl"></div>
<div class="abs svc-line"></div>

<div class="abs svc" style="left:182px;top:1358px">
  <svg class="hex" width="46" height="50" viewBox="0 0 46 50"><path d="M23 2l20 11v24L23 48 3 37V13z" fill="#fff" stroke="#1e62a8" stroke-width="2"/><circle cx="23" cy="25" r="7" fill="#1e62a8"/></svg>
  <h4 style="top:-2px">Technology</h4>
  <p style="top:24px">Lantern Advisory Training programs are perfect for individuals</p>
</div>
<div class="abs svc" style="left:474px;top:1352px">
  <svg class="hex" width="46" height="50" viewBox="0 0 46 50"><path d="M23 2l20 11v24L23 48 3 37V13z" fill="none" stroke="#1e62a8" stroke-width="2"/><rect x="14" y="18" width="18" height="14" fill="#1e62a8"/></svg>
  <h4 style="top:4px">Business</h4>
  <p style="top:28px">Our Offshore development model has a unique distinction</p>
</div>
<div class="abs svc" style="left:764px;top:1352px">
  <svg class="hex" width="46" height="50" viewBox="0 0 46 50"><path d="M23 2l20 11v24L23 48 3 37V13z" fill="none" stroke="#1e62a8" stroke-width="2"/><circle cx="23" cy="25" r="8" fill="none" stroke="#1e62a8" stroke-width="3"/></svg>
  <h4 style="top:4px">Application<br>Development</h4>
  <p style="top:44px">Drawing on our experience in all major industries, we develop</p>
</div>
<div class="abs svc" style="left:182px;top:1524px">
  <svg class="hex" width="46" height="50" viewBox="0 0 46 50"><path d="M23 2l20 11v24L23 48 3 37V13z" fill="none" stroke="#1e62a8" stroke-width="2"/><circle cx="23" cy="25" r="8" fill="#1e62a8"/><circle cx="23" cy="25" r="3" fill="#fff"/></svg>
  <h4 style="top:6px">Enterprise<br>Integration</h4>
  <p style="top:46px">As organizations work to achieve and sustain competitive</p>
</div>
<div class="abs svc" style="left:474px;top:1524px">
  <svg class="hex" width="46" height="50" viewBox="0 0 46 50"><path d="M23 2l20 11v24L23 48 3 37V13z" fill="none" stroke="#1e62a8" stroke-width="2"/><rect x="14" y="17" width="18" height="12" fill="none" stroke="#1e62a8" stroke-width="2"/><rect x="11" y="31" width="24" height="3" fill="#1e62a8"/></svg>
  <h4 style="top:6px">IT Consulting</h4>
  <p style="top:30px">Information technology should improve business results</p>
</div>
<div class="abs svc" style="left:764px;top:1524px">
  <svg class="hex" width="46" height="50" viewBox="0 0 46 50"><path d="M23 2l20 11v24L23 48 3 37V13z" fill="none" stroke="#1e62a8" stroke-width="2"/><circle cx="23" cy="25" r="8" fill="none" stroke="#1e62a8" stroke-width="2"/><circle cx="23" cy="25" r="4" fill="none" stroke="#1e62a8" stroke-width="2"/></svg>
  <h4 style="top:6px">Research</h4>
  <p style="top:30px">we're helping you solve your business challenges today</p>
</div>

<div class="abs testi"></div>
<div class="abs sec-title testi-title">Testimonials</div>
<div class="abs t-photo p1" role="img" aria-label="Portrait photo of a company CEO"></div>
<div class="abs t-body" style="left:399px">
  <h5>Daniel Royce</h5><div class="role">CEO &amp; MD</div>
  <p>Lorem ipsum dolor sit amet, tetuer adipiscing elit, sed diam lonummy nibh euismod tincidunt ut laoreet dolore magna aliquam erat lutpat.</p>
</div>
<div class="abs t-photo p2" role="img" aria-label="Portrait photo of a managing director"></div>
<div class="abs t-body" style="left:839px">
  <h5>Elena Marsh</h5><div class="role">Managing Director</div>
  <p>Lorem ipsum dolor sit amet, tetuer adipiscing elit, sed diam lonummy nibh euismod tincidunt ut laoreet dolore magna aliquam erat lutpat.</p>
</div>

<div class="abs callback"></div>
<h2 class="abs callback-title">Request a call<br>back</h2>
<div class="abs callback-label">I would like to discuss</div>
<ul class="abs select">
  <li class="top">Technology</li>
  <li class="active">Business</li>
  <li>Application Development</li>
  <li>Enterprise Integration</li>
  <li>IT Consulting</li>
</ul>
<div class="abs input callback-name">Name</div>
<div class="abs btn callback-btn">SUBMIT</div>

<div class="abs map" role="img" aria-label="Street map showing the head office location"></div>

<div class="abs offices"></div>
<div class="abs divider-v" style="left:431px"></div>
<div class="abs divider-v" style="left:726px"></div>
<div class="abs office" style="left:184px">
  <h3>Head Office</h3>
  <div class="row"><span>●</span>410 Harbor Lane Suite 12<br>Eastbrook, NJ 07000</div>
  <div class="row"><span>●</span>+1 (555) 014 2290</div>
  <div class="row"><span>●</span>info@lanternadvisoryinc.example</div>
</div>
<div class="abs office" style="left:476px">
  <h3>Technical Center</h3>
  <div class="row"><span>●</span>8820 W Cedar Road, Suite 140<br>Millbrook MI 48000</div>
  <div class="row"><span>●</span>+1 (555) 014 2290</div>
  <div class="row"><span>●</span>tech@lanternadvisoryinc.example</div>
</div>
<div class="abs office" style="left:766px">
  <h3>West Coast Office</h3>
  <div class="row"><span>●</span>275 Summit Place Suite 300<br>Bayview CA 95000</div>
  <div class="row"><span>●</span>+1 (555) 014 2290</div>
  <div class="row"><span>●</span>wc@lanternadvisoryinc.example</div>
</div>

<div class="abs footer"></div>
<div class="abs brand footer-brand"><span class="mark"></span>Lantern Advisory</div>
<p class="abs footer-about">Today's IT market is a dynamic, fast paced industry, with ever-increasing demands. Meeting these demands for over 25 years, Lantern Advisory maintains a global presence, aggressively [...]</p>
<div class="abs f-col" style="left:399px">
  <h6>Links</h6>
  <ul><li>Mission &amp; Vision</li><li>Focus</li><li>Services</li><li>Solutions</li><li>Our process</li><li>Staff Augmentation</li><li>Career</li></ul>
</div>
<div class="abs f-col" style="left:619px">
  <h6>FAQ</h6>
  <p>So just what is the Lantern Advisory way?</p>
  <p style="margin-top:8px">Whether different industries, different financial concerns, different personalities [...]</p>
</div>
<div class="abs f-col" style="left:837px"><h6>Subscribe</h6></div>
<div class="abs sub-input">Email id</div>
<div class="abs sub-btn"></div>
<div class="abs sub-note">Get latest updates</div>

<div class="abs copy"></div>
<div class="abs copy-txt">Copyright © 2016 Lanternadvisoryinc</div>
<div class="abs copy-social"><span></span><span></span><span></span><span></span></div>

</body>
</html>
```